Artificial intelligence, machine learning, and automation company needs a sexy business card design

We need a sleek and sexy business card design for an AI consulting company based in Philadelphia PA. We provide custom machine learning and automation solutions for companies of all shapes and sizes. The primary industries that we serve are pharmaceuticals, engineering, healthcare, and computer software. We would like the designs to be a black business card that uses green as a sleek accent color. The final design should communicate intelligence, cutting edge new-tech, and optimization.

Target Market(s)

C-level and VP level executives of multi-million annual companies. Mostly in Pharma, Healthcare, Real Estate, Retail, and Engineering

Industry/Entity Type

Computer Software

Contact Information for Business Card

Name: Jed Harlow
Title: CEO
Cell: 484 562 0937
Email: JedH@quillorbit.example
Website: www.QuillOrbit.example

Font styles to use
Sans Serif

Colors

Designer to choose colors to be used in the design.

Requirements
Must have
• 1) Attached Quillon Logo (either with colors or not/embossed)
• 2) "Artificial Intelligence" "Automation" and "Machine Learning"
• 3) "Quillon Laboratories" or "Quillon Labs" or "Quillon"
• 4) Sexy AF.
Nice to have
• Black card / dark card color, "Quillon Green" accent colors (in attached .ai file), Embossment of logo/name/etc, thick card stock, colored borders (on card sides, not front/back faces)
Should not have
• Should not be bland, or unsexy.

```html
<!DOCTYPE html>
<html lang="en">
<head>
<meta charset="utf-8">
<title>Quillon Laboratories – Business Card</title>
<link rel="stylesheet" href="https://fonts.googleapis.com/css2?family=Roboto:wght@400;500;700&display=swap">
<style>
  :root {
    --page-bg: #1c1e20;
    --card-bg: #141414;
    --quillon-green: #3fc1a9;
    --accent-orange: #e0902a;
    --text-light: #d8d8d8;
    --text-muted: #a9a9a9;
    --emboss: #4a4a4a;
  }
  * { margin: 0; padding: 0; box-sizing: border-box; }
  html, body { width: 1200px; height: 900px; overflow: hidden; }
  body {
    background: var(--page-bg);
    font-family: "Roboto", Arial, sans-serif;
    display: flex;
    flex-direction: column;
    align-items: center;
    justify-content: center;
    gap: 56px;
  }
  .card {
    position: relative;
    width: 600px;
    height: 343px;
    background: var(--card-bg);
    box-shadow: 0 10px 30px rgba(0,0,0,0.45);
  }

  /* Front: contact side */
  .identity {
    position: absolute;
    left: 70px;
    top: 88px;
    text-align: right;
  }
  .identity__name {
    color: var(--quillon-green);
    font-weight: 500;
    font-size: 36px;
    letter-spacing: 0.5px;
    text-transform: uppercase;
    line-height: 1;
  }
  .identity__title {
    color: var(--text-light);
    font-size: 17px;
    margin-top: 10px;
    padding-right: 4px;
  }
  .divider {
    position: absolute;
    left: 300px;
    top: 160px;
    width: 3px;
    height: 76px;
    background: var(--accent-orange);
  }
  .contacts {
    position: absolute;
    left: 322px;
    top: 158px;
    list-style: none;
  }
  .contacts__item {
    display: flex;
    align-items: center;
    gap: 12px;
    color: var(--text-light);
    font-size: 17px;
    height: 27px;
  }
  .contacts__icon { width: 18px; height: 18px; flex: none; }
  .contacts__site { color: var(--quillon-green); }

  /* Back: brand side */
  .brand {
    position: absolute;
    left: 0; right: 0;
    top: 82px;
    display: flex;
    justify-content: center;
    align-items: center;
    gap: 22px;
  }
  .brand__square {
    width: 72px;
    height: 72px;
    border: 3px solid var(--emboss);
  }
  .brand__name {
    color: var(--emboss);
    font-weight: 500;
    text-transform: uppercase;
    line-height: 1.1;
  }
  .brand__name-main { display: block; font-size: 42px; letter-spacing: 9px; }
  .brand__name-sub { display: block; font-size: 15px; letter-spacing: 8px; }
  .brand__site {
    position: absolute;
    left: 0; right: 0;
    top: 232px;
    text-align: center;
    color: var(--text-light);
    font-size: 20px;
  }
  .brand__site span { color: var(--quillon-green); }
</style>
</head>
<body>

  <section class="card card--front">
    <div class="identity">
      <div class="identity__name">Jed Harlow</div>
      <div class="identity__title">CEO</div>
    </div>
    <div class="divider"></div>
    <ul class="contacts">
      <li class="contacts__item">
        <svg class="contacts__icon" viewBox="0 0 18 18" aria-hidden="true">
          <rect x="2" y="4" width="14" height="10" fill="none" stroke="#3fc1a9" stroke-width="1.8"/>
          <path d="M2 4 L9 10 L16 4 M2 14 L7 9 M16 14 L11 9" fill="none" stroke="#3fc1a9" stroke-width="1.6"/>
        </svg>
        JedH@quillorbit.example
      </li>
      <li class="contacts__item">
        <svg class="contacts__icon" viewBox="0 0 18 18" aria-hidden="true">
          <path d="M5 2 L7.5 5.5 L6 7.5 Q8 11 10.5 12 L12.5 10.5 L16 13 L14 16 Q6 15 2.5 5 Z" fill="#3fc1a9"/>
        </svg>
        484 562 0937
      </li>
      <li class="contacts__item">
        <svg class="contacts__icon" viewBox="0 0 18 18" aria-hidden="true">
          <circle cx="9" cy="9" r="8" fill="#3fc1a9"/>
          <path d="M1 9 H17 M9 1 Q4 9 9 17 M9 1 Q14 9 9 17" fill="none" stroke="#141414" stroke-width="1.2"/>
        </svg>
        <span>www.<span class="contacts__site">QuillOrbit</span>.example</span>
      </li>
    </ul>
  </section>

  <section class="card card--back">
    <div class="brand">
      <div class="brand__square"></div>
      <div class="brand__name">
        <span class="brand__name-main">Quillon</span>
        <span class="brand__name-sub">Laboratories</span>
      </div>
    </div>
    <div class="brand__site">www.<span>quillorbit</span>.example</div>
  </section>

</body>
</html>
```